Therapy Dog Organization Website

Looking for a website that is user friendly, welcoming, dog themed and has the following pages and links:
*Click here to join - links to a jot form
*Click here to donate - links to our paypal page
*Request a visit - links to a jot form
*Facebook Follow Link
*Instagram Follow Link
*Our team - images uploaded to showcase our dogs
*Donors and Referrals Page - Where I can update as donations and referrals come in.
*Online store. Currently this is in Jot Form but I would like a store front. I would not want this to be a link but rather a hidden page, something like www.brightmeadow.org/teamstore.

Please visit www.brightmeadow.org to see what we have right now designed simply in Canva. Dog photos can be provided to use in images.

Note: I have funds from a grant that I have to spend to add gratuity to the project winner.

```html
<!DOCTYPE html>
<html lang="en">
<head>
<meta charset="utf-8">
<title>Bright Meadow Therapy Dogs</title>
<link href="https://fonts.googleapis.com/css2?family=Outfit:wght@500;600;700&family=Nunito:wght@400;600;700;800&display=swap" rel="stylesheet">
<style>
:root{
  --navy:#14232e;
  --navy-2:#1b2c38;
  --teal:#1c6b6d;
  --teal-2:#2a8a87;
  --mint:#e8f7f5;
  --mint-2:#bfe9e3;
  --orange:#f47b20;
  --cream:#fff8ec;
  --ink:#1d2a33;
  --muted:#5c6870;
  --line:#e4ebee;
  --white:#ffffff;
}
*{box-sizing:border-box;margin:0;padding:0}
html,body{width:1200px;height:5013px;overflow:hidden}
body{font-family:'Nunito',sans-serif;color:var(--ink);background:var(--white)}
h1,h2,h3,.display{font-family:'Outfit',sans-serif}
.eyebrow{font-size:9px;font-weight:800;letter-spacing:1.6px;color:var(--orange);text-transform:uppercase}
.btn{display:inline-flex;align-items:center;justify-content:center;height:32px;padding:0 18px;border-radius:16px;font-size:10px;font-weight:800;text-decoration:none}
.btn-orange{background:var(--orange);color:#fff}
.btn-ghost{border:1.5px solid rgba(255,255,255,.6);color:#fff}
.btn-white{background:#fff;color:var(--teal)}
.ph{position:relative;overflow:hidden}
.ph .cap{position:absolute;left:8px;bottom:8px;color:#fff;font-size:8px;font-weight:700}
/* hero */
.hero{height:620px;position:relative;background:radial-gradient(ellipse at 72% 35%,#4a5a66 0%,#2a3742 40%,#18242e 80%);color:#fff}
.hero-photo{position:absolute;inset:0;background:linear-gradient(90deg,rgba(20,32,42,.92) 0%,rgba(20,32,42,.55) 55%,rgba(20,32,42,.3) 100%)}
.nav{position:absolute;top:28px;left:220px;right:220px;height:34px;display:flex;align-items:center}
.brand{font-family:'Outfit',sans-serif;font-weight:600;font-size:19px;color:#fff;display:flex;align-items:center;gap:7px;line-height:1}
.brand small{display:block;font-size:9px;letter-spacing:1.5px}
.brand .dot{width:14px;height:14px;border-radius:50%;background:#fff}
.nav ul{list-style:none;display:flex;gap:18px;margin-left:60px;font-size:9px;font-weight:700}
.nav .acts{margin-left:auto;display:flex;gap:8px}
.nav .btn{height:24px;padding:0 14px;font-size:8px}
.btn-outline-teal{border:1.5px solid var(--teal-2);color:#9fe0d8}
.hero-copy{position:absolute;left:220px;top:176px;width:420px}
.pill{display:inline-block;background:rgba(255,255,255,.12);border-radius:10px;padding:3px 10px;font-size:7px;font-weight:800;letter-spacing:1px}
.hero h1{font-size:36px;line-height:41px;font-weight:700;margin-top:14px}
.hero p{font-size:12px;line-height:18px;margin-top:16px;opacity:.9;width:330px}
.hero .ctas{display:flex;gap:10px;margin-top:18px;align-items:center}
.hero .link{font-size:10px;font-weight:800;color:#fff;border-bottom:1.5px solid var(--orange);margin-left:16px}
.follow{display:flex;align-items:center;gap:8px;margin-top:22px;font-size:9px}
.soc{width:26px;height:26px;border-radius:50%;background:rgba(255,255,255,.14);display:inline-flex;align-items:center;justify-content:center}
.soc i{width:8px;height:8px;border-radius:50%;background:#fff;display:block}
.scroll{position:absolute;left:0;right:0;top:566px;text-align:center;font-size:7px;letter-spacing:1.5px;opacity:.75}
.strip{height:42px;background:var(--teal);display:flex;justify-content:center;align-items:center;gap:32px;color:#fff;font-size:9px;font-weight:700}
.strip span::before{content:"";display:inline-block;width:6px;height:6px;border-radius:50%;background:var(--orange);margin-right:6px;vertical-align:1px}
/* story */
.story{height:593px;position:relative}
.story-frame{position:absolute;left:210px;top:60px;width:382px;height:468px;background:var(--mint-2);border-radius:16px;padding:10px}
.story-photo{width:100%;height:100%;border-radius:12px;background:linear-gradient(180deg,#e9eef2 0%,#c9d3da 45%,#3a6fd0 60%,#9a7a4c 85%,#6c6c70 100%)}
.badge{position:absolute;left:458px;top:492px;background:#fff;border-radius:8px;box-shadow:0 4px 14px rgba(0,0,0,.12);padding:8px 12px;font-size:8px;font-weight:800;display:flex;gap:8px;align-items:center}
.badge i{width:18px;height:18px;border-radius:50%;background:#d9a764;display:block}
.badge small{display:block;font-weight:600;color:var(--muted);font-size:7px}
.story-copy{position:absolute;left:617px;top:168px;width:370px}
.story-copy h2{font-size:21px;margin-top:8px;font-weight:700}
.story-copy p{font-size:10px;line-height:17px;color:var(--muted);margin-top:16px}
.story-copy a{display:block;margin-top:18px;font-size:9px;font-weight:800;color:var(--teal);text-decoration:none}
/* mission */
.mission{height:428px;background:var(--mint);text-align:center;padding-top:71px}
.mission h2{font-size:21px;margin-top:10px}
.cards2{display:flex;gap:20px;margin:36px auto 0;width:760px;text-align:left}
.mcard{flex:1;background:#fff;border-radius:12px;padding:26px 24px;height:210px;box-shadow:0 2px 10px rgba(0,0,0,.04)}
.mcard .ic{width:34px;height:34px;border-radius:8px}
.mcard h3{font-size:14px;margin-top:18px}
.mcard p{font-size:8.5px;line-height:15px;color:var(--muted);margin-top:10px}
/* community */
.community{height:854px;text-align:center;padding-top:72px}
.community h2{font-size:21px;margin-top:10px}
.community .lead{font-size:10px;line-height:17px;color:var(--muted);width:420px;margin:10px auto 0}
.grid{display:grid;grid-template-columns:180px 180px 181px 181px;grid-auto-rows:138px;gap:12px;width:760px;margin:34px auto 0}
.grid .ph{border-radius:6px;text-align:left}
.big{grid-column:span 2;grid-row:span 2}
.wide{grid-column:span 2}
/* team */
.team{height:983px;background:var(--navy);color:#fff;text-align:center;padding-top:72px}
.team h2{font-size:21px;margin-top:6px}
.team .lead{font-size:10px;line-height:17px;opacity:.75;margin-top:8px}
.dogs{display:grid;grid-template-columns:repeat(5,140px);column-gap:15px;row-gap:14px;width:760px;margin:32px auto 0}
.dog{height:210px}
.dcard{height:186px;border-radius:6px;background:#c6ecf0;padding:6px;position:relative}
.dcard .in{height:100%;border-radius:4px;background:linear-gradient(180deg,#3e7fd2,#2a5ea8);padding:4px;display:flex;flex-direction:column}
.dcard .nm{font-family:'Outfit',sans-serif;font-weight:700;font-size:15px;color:#fff;height:22px;line-height:22px}
.dcard .photo{flex:1;border-radius:3px}
.dcard .ribbon{height:24px;margin-top:4px;background:#2b63c4;border-radius:3px}
.dog .label{font-size:8px;font-weight:800;margin-top:9px}
.team .btn{margin-top:22px;background:var(--teal-2);color:#fff}
/* donors */
.donors{height:570px;background:var(--cream);text-align:center;padding-top:70px}
.donors h2{font-size:21px;margin-top:8px}
.donors .lead{font-size:10px;line-height:17px;color:var(--muted);width:500px;margin:12px auto 0}
.cards3{display:flex;gap:20px;width:760px;margin:40px auto 0;text-align:left}
.dc{flex:1;background:#fff;border-radius:12px;padding:22px 20px;height:225px;box-shadow:0 2px 10px rgba(0,0,0,.04)}
.dc h3{font-size:11px;display:flex;align-items:center;gap:6px}
.dc h3 i{width:10px;height:10px;border-radius:50%;display:block}
.dc b{display:block;font-size:9px;margin-top:16px}
.dc small{display:block;font-size:7.5px;color:var(--muted);line-height:12px;margin-top:3px}
.dc ul{list-style:none;margin-top:12px}
.dc li{font-size:8.5px;color:var(--muted);height:22px;display:flex;align-items:center;gap:8px}
.dc li::before{content:"";width:6px;height:6px;border-radius:50%;background:var(--teal-2)}
.donors .note{font-size:8.5px;color:var(--muted);margin-top:28px}
.donors .note u{color:var(--teal);font-weight:800}
/* cta */
.cta{height:248px;background:var(--teal);color:#fff;text-align:center;padding-top:68px}
.cta h2{font-size:21px}
.cta p{font-size:10px;line-height:17px;opacity:.9;width:420px;margin:8px auto 0}
.cta .row{display:flex;gap:10px;justify-content:center;margin-top:20px}
/* contact */
.contact{height:412px;padding-top:70px}
.ccard{width:760px;height:272px;margin:0 auto;background:var(--navy);border-radius:14px;color:#fff;text-align:center;padding-top:42px}
.ccard h2{font-size:21px;margin-top:8px}
.ccard p{font-size:9.5px;line-height:16px;opacity:.8;width:380px;margin:10px auto 0}
.ccard .btn{margin-top:16px;width:204px}
.ccard .socs{display:flex;gap:16px;justify-content:center;margin-top:20px}
/* footer */
.footer{height:263px;background:var(--navy);color:#fff;position:relative}
.footer .col{position:absolute;top:46px}
.footer .about{left:220px;width:250px}
.footer .about p{font-size:9px;line-height:15px;opacity:.75;margin-top:12px}
.footer .about .socs{display:flex;gap:10px;margin-top:12px}
.footer h4{font-size:9px;font-weight:800}
.footer .links a{display:block;font-size:9px;opacity:.75;margin-top:12px;color:#fff;text-decoration:none}
.footer .bottom{position:absolute;left:220px;right:220px;bottom:22px;display:flex;justify-content:space-between;font-size:7.5px;opacity:.6;border-top:1px solid rgba(255,255,255,.1);padding-top:14px}
</style>
</head>
<body>

<header class="hero">
  <div class="hero-photo" role="img" aria-label="Photo of a team mascot in a school gym, dimmed behind the headline"></div>
  <nav class="nav">
    <div class="brand"><span class="dot"></span><span>Bright Meadow<small>Therapy Dogs</small></span></div>
    <ul><li>Our Story</li><li>Mission</li><li>What We Do</li><li>Our Team</li><li>Donors</li><li>Contact</li></ul>
    <div class="acts"><a class="btn btn-outline-teal">Join Our Pack</a><a class="btn btn-orange">Donate</a></div>
  </nav>
  <div class="hero-copy">
    <span class="pill">● A MICHIGAN NONPROFIT</span>
    <h1>Bringing comfort, joy<br>&amp; unconditional love —<br>one paw at a time.</h1>
    <p>A Michigan nonprofit dedicated to providing therapy dogs to the community to spread joy, hope and healing.</p>
    <div class="ctas">
      <a class="btn btn-orange">Request a Visit →</a>
      <a class="btn btn-ghost">Click Here to Join!</a>
      <a class="link">Click Here to Donate!</a>
    </div>
    <div class="follow">Follow the Pack: <span class="soc"><i></i></span><span class="soc"><i></i></span></div>
  </div>
  <div class="scroll">SCROLL<br>⌄</div>
</header>

<div class="strip"><span>Hospitals</span><span>Schools</span><span>Senior Communities</span><span>Certified Therapy Teams</span><span>Michigan Nonprofit</span></div>

<section class="story">
  <div class="story-frame"><div class="story-photo" role="img" aria-label="Two golden retrievers sitting beside a blue table with the organization's banner"></div></div>
  <div class="badge"><i></i><span>15+ Pack Members<small>certified &amp; growing</small></span></div>
  <div class="story-copy">
    <div class="eyebrow">Our Story</div>
    <h2>Every wag tells a story.</h2>
    <p>Ours began with a simple belief: the love of a dog can change lives. What started with a few volunteers and their dogs has grown into a community dedicated to bringing comfort and joy wherever it's needed most.</p>
    <p>From hospitals to schools and senior centers, our therapy dog teams share moments of connection, calm, and healing — one visit at a time. At the heart of our mission is a simple truth: sometimes the best kind of therapy comes with four paws and a wagging tail.</p>
    <a>Read our mission &amp; purpose →</a>
  </div>
</section>

<section class="mission">
  <div class="eyebrow">Why We're Here</div>
  <h2>Our mission &amp; purpose</h2>
  <div class="cards2">
    <div class="mcard"><div class="ic" style="background:var(--teal)"></div><h3>Our Mission</h3><p>To certify and deploy therapy dog teams that promote emotional well-being, reduce stress, and foster empathy. We are dedicated to improving quality of life by bringing the unconditional love and calming presence of therapy dogs to those in need, while upholding the highest standards of animal welfare, professionalism, and community service.</p></div>
    <div class="mcard"><div class="ic" style="background:var(--orange)"></div><h3>Our Purpose</h3><p>Our purpose is to share the comfort, joy, and healing power of the human-animal bond. We connect trained therapy dog teams with people in need of emotional support, companionship, and encouragement in hospitals, schools, senior communities, and beyond — lifting spirits and easing stress, one visit at a time.</p></div>
  </div>
</section>

<section class="community">
  <div class="eyebrow">Out &amp; About</div>
  <h2>Spreading joy across our community</h2>
  <p class="lead">From classrooms to courtside, our pack shows up wherever a wagging tail can make someone's day.</p>
  <div class="grid">
    <div class="ph big" role="img" aria-label="Volunteers with therapy dogs visiting a classroom" style="background:linear-gradient(160deg,#8a8f95,#3d4248 60%,#5a4a3c)"><span class="cap">Classroom comfort visits</span></div>
    <div class="ph" role="img" aria-label="Dogs on a college basketball court" style="background:linear-gradient(180deg,#2f5fb0,#c8a26a)"><span class="cap">Campus &amp; game-day visits</span></div>
    <div class="ph" role="img" aria-label="Group of dogs on a lawn with first responders" style="background:linear-gradient(180deg,#8fa3b0,#6f7f4a)"><span class="cap">First responder visits</span></div>
    <div class="ph" role="img" aria-label="The pack together indoors" style="background:linear-gradient(180deg,#d8dde0,#8a7d6c)"><span class="cap">The pack, together</span></div>
    <div class="ph" role="img" aria-label="Dog at a school event" style="background:linear-gradient(180deg,#3b4c7a,#3a8fd0)"><span class="cap">School &amp; event visits</span></div>
    <div class="ph" role="img" aria-label="Dogs in vests on a blanket" style="background:linear-gradient(180deg,#8c8c8c,#2f9fbf)"><span class="cap">Happy &amp; calm moments</span></div>
    <div class="ph" role="img" aria-label="Dogs in vests ready to visit" style="background:linear-gradient(180deg,#b5a48c,#c84a3a)"><span class="cap">Vested &amp; ready to visit</span></div>
    <div class="ph" role="img" aria-label="Dog resting after a visit" style="background:linear-gradient(180deg,#7a8fa0,#3a6fb0)"><span class="cap">Full of energy off-duty</span></div>
    <div class="ph" role="img" aria-label="Dogs at a car show" style="background:linear-gradient(180deg,#a8b8c4,#4a5a7a)"><span class="cap">Community events &amp; car shows</span></div>
    <div class="ph wide" role="img" aria-label="Dog on a senior community visit" style="background:linear-gradient(160deg,#4a3a2e,#a08060)"><span class="cap">Senior community visits</span></div>
    <div class="ph" role="img" aria-label="Handlers with their dogs" style="background:linear-gradient(180deg,#5a6070,#2a3a5a)"><span class="cap">Handlers &amp; their pups</span></div>
    <div class="ph" role="img" aria-label="Dog beside a holiday tree" style="background:linear-gradient(180deg,#c8ccd0,#3a6a7a)"><span class="cap">Holiday hospital visits</span></div>
  </div>
</section>

<section class="team">
  <div class="eyebrow">Meet the Pack</div>
  <h2>Our Team</h2>
  <p class="lead">Every member of our pack is a certified therapy dog with a heart for helping others.<br>Say hello to a few of our good boys and girls!</p>
  <div class="dogs">
    <div class="dog"><div class="dcard"><div class="in"><div class="nm">Juniper</div><div class="photo" role="img" aria-label="Portrait of Juniper, a black dog" style="background:linear-gradient(180deg,#6f8a5a,#1e1e20)"></div><div class="ribbon"></div></div></div><div class="label">Juniper</div></div>
    <div class="dog"><div class="dcard"><div class="in"><div class="nm">Biscuit</div><div class="photo" role="img" aria-label="Portrait of Biscuit, a tan dog" style="background:linear-gradient(180deg,#8a6a4a,#c09060)"></div><div class="ribbon"></div></div></div><div class="label">Biscuit</div></div>
    <div class="dog"><div class="dcard"><div class="in"><div class="nm">Pepper</div><div class="photo" role="img" aria-label="Portrait of Pepper, a black and white dog" style="background:linear-gradient(180deg,#7a9a5a,#2a2a2a)"></div><div class="ribbon"></div></div></div><div class="label">Pepper</div></div>
    <div class="dog"><div class="dcard"><div class="in"><div class="nm">Clover</div><div class="photo" role="img" aria-label="Portrait of Clover, a small fluffy dog" style="background:linear-gradient(180deg,#e0d0b0,#c07a3a)"></div><div class="ribbon"></div></div></div><div class="label">Clover</div></div>
    <div class="dog"><div class="dcard"><div class="in"><div class="nm">Scout</div><div class="photo" role="img" aria-label="Portrait of Scout, a grey and white dog" style="background:linear-gradient(180deg,#8a8a7a,#4a4a50)"></div><div class="ribbon"></div></div></div><div class="label">Scout</div></div>
    <div class="dog"><div class="dcard"><div class="in"><div class="nm">Willow</div><div class="photo" role="img" aria-label="Portrait of Willow, a long-haired dog" style="background:linear-gradient(180deg,#6a5a4a,#b08a5a)"></div><div class="ribbon"></div></div></div><div class="label">Willow</div></div>
    <div class="dog"><div class="dcard"><div class="in"><div class="nm">Honeybee</div><div class="photo" role="img" aria-label="Portrait of Honeybee, a curly golden dog" style="background:linear-gradient(180deg,#c8b090,#d0a070)"></div><div class="ribbon"></div></div></div><div class="label">Honeybee</div></div>
    <div class="dog"><div class="dcard"><div class="in"><div class="nm">Maple</div><div class="photo" role="img" aria-label="Portrait of Maple, a golden dog" style="background:linear-gradient(180deg,#b09a80,#d8b080)"></div><div class="ribbon"></div></div></div><div class="label">Maple</div></div>
    <div class="dog"><div class="dcard"><div class="in"><div class="nm">Frost</div><div class="photo" role="img" aria-label="Portrait of Frost, a white dog" style="background:linear-gradient(180deg,#8aa070,#e8e4dc)"></div><div class="ribbon"></div></div></div><div class="label">Frost</div></div>
    <div class="dog"><div class="dcard"><div class="in"><div class="nm">Copper</div><div class="photo" role="img" aria-label="Portrait of Copper, a curly red dog" style="background:linear-gradient(180deg,#8a7a6a,#a0603a)"></div><div class="ribbon"></div></div></div><div class="label">Copper</div></div>
    <div class="dog"><div class="dcard"><div class="in"><div class="nm">Daisy</div><div class="photo" role="img" aria-label="Portrait of Daisy, a cream dog" style="background:linear-gradient(180deg,#a0b0c0,#f0e4d0)"></div><div class="ribbon"></div></div></div><div class="label">Daisy</div></div>
    <div class="dog"><div class="dcard"><div class="in"><div class="nm">Nutmeg</div><div class="photo" role="img" aria-label="Portrait of Nutmeg, a small tan and white dog" style="background:linear-gradient(180deg,#7a9a6a,#d8b890)"></div><div class="ribbon"></div></div></div><div class="label">Nutmeg</div></div>
    <div class="dog"><div class="dcard"><div class="in"><div class="nm">Sunny</div><div class="photo" role="img" aria-label="Portrait of Sunny, a golden dog in a vest" style="background:linear-gradient(180deg,#6a8a5a,#c09050)"></div><div class="ribbon"></div></div></div><div class="label">Sunny</div></div>
    <div class="dog"><div class="dcard"><div class="in"><div class="nm">Pebble</div><div class="photo" role="img" aria-label="Portrait of Pebble, a pale puppy" style="background:linear-gradient(180deg,#b0a090,#efe6da)"></div><div class="ribbon"></div></div></div><div class="label">Pebble</div></div>
    <div class="dog"><div class="dcard"><div class="in"><div class="nm">Cocoa</div><div class="photo" role="img" aria-label="Portrait of Cocoa, a chocolate dog" style="background:linear-gradient(180deg,#9aa0a8,#5a3a2a)"></div><div class="ribbon"></div></div></div><div class="label">Cocoa</div></div>
  </div>
  <a class="btn">Think your pup has what it takes? Join the pack</a>
</section>

<section class="donors">
  <div class="eyebrow" style="color:var(--teal)">With Gratitude</div>
  <h2>Donors &amp; Referrals</h2>
  <p class="lead">Our donors and referral partners are the heart of our organization. Because of their generosity, we're able to keep costs low for our therapy dog teams while never compromising the integrity, training, and care of our handlers and dogs. Thank you for believing in our mission and helping us spread healing one paw at a time.</p>
  <div class="cards3">
    <div class="dc"><h3><i style="background:var(--teal-2)"></i>Corporate Donors</h3>
      <b>Lumina Tel</b><small>Cloud phone systems built for reliable business communications.</small>
      <b>Harlow-Bennett Post 71, Veterans Hall</b><small>Serving veterans from the local community since 1930. To all who have served America: thank you!</small></div>
    <div class="dc"><h3><i style="background:#f4c430"></i>Individual Donors</h3>
      <ul><li>Martin Hale</li><li>Owen Draper</li><li>Walter Hale</li><li>Grace Whitlow</li><li>Lena Marsh</li><li>Peter Hale</li><li>Curt Ellison</li></ul></div>
    <div class="dc"><h3><i style="background:var(--orange)"></i>Referrals</h3>
      <b>Steadfast Canine Training</b><small>Northern Michigan dog training facility — bridging the communication gap between dogs &amp; owners.</small></div>
  </div>
  <p class="note">Want to support our pack? <u>Click here to donate</u> or <u>contact us</u> about becoming a referral partner.</p>
</section>

<section class="cta">
  <h2>Ready to spread some joy?</h2>
  <p>Whether you'd love a visit, want to join our pack with your pup, or simply want to help us keep going — there's a place for you here.</p>
  <div class="row"><a class="btn btn-white">Request a Visit</a><a class="btn btn-orange">Click Here to Join!</a><a class="btn btn-ghost">Click Here to Donate!</a></div>
</section>

<section class="contact">
  <div class="ccard">
    <div class="eyebrow">Get in Touch</div>
    <h2>Contact Us</h2>
    <p>Have a question about scheduling a visit, joining the pack, or partnering with Bright Meadow? We'd love to hear from you.</p>
    <a class="btn btn-orange">Please Click Here to Contact Us →</a>
    <div class="socs"><span class="soc"><i></i></span><span class="soc"><i></i></span></div>
  </div>
</section>

<footer class="footer">
  <div class="col about">
    <div class="brand"><span class="dot"></span><span>Bright Meadow<small>Therapy Dogs</small></span></div>
    <p>A Michigan nonprofit dedicated to providing therapy dogs to the community to spread joy, hope and healing — one paw at a time.</p>
    <div class="socs"><span class="soc"><i></i></span><span class="soc"><i></i></span></div>
  </div>
  <div class="col links" style="left:612px"><h4>Explore</h4><a>Our Story</a><a>Mission &amp; Purpose</a><a>What We Do</a><a>Our Team</a><a>Donors &amp; Referrals</a></div>
  <div class="col links" style="left:808px"><h4>Get Involved</h4><a>Join Our Pack</a><a>Request a Visit</a><a>Donate</a><a>Contact Us</a></div>
  <div class="bottom"><span>© 2026 Bright Meadow Therapy Dogs. A Michigan nonprofit. All rights reserved.</span><span>Made with care for people &amp; pups alike.</span></div>
</footer>

</body>
</html>
```